Travel Blogger Business Card for roamquill.net

I need a two-sided business card for a travel blogging website. The card should be both professional and fun at the same time. This is for the website www.roamquill.net

I don't necessarily think that the current logo on the website needs to be used on the business card but it can be. I am very flexible with ideas

Target Market(s)

Travel agencies that will be met at a conference.

Industry/Entity Type

Travel

Contact Information for Business Card

Company Name: Roam Quill.net
Name: Bertrand Olesky
Voice: +1-(345)-402-7731
Address: Coral Reach Shore, Grand Cayman, Cayman Islands
Email: ceo@roamquill.net

Colors
0592cd
0355a3
3176b5
33a6d7
85cae6
85acd3

Requirements
Must have
• Website address and name should be bigger than address, phone number, and email.

```html
<!DOCTYPE html>
<html lang="en">
<head>
<meta charset="utf-8">
<title>Roam Quill – Business Card</title>
<link rel="stylesheet" href="https://fonts.googleapis.com/css2?family=Open+Sans:wght@400;600&family=Roboto:wght@700&display=swap">
<style>
  :root {
    --brand-blue: #1ba4d2;
    --brand-blue-soft: rgba(27, 164, 210, 0.95);
    --brand-blue-fade: rgba(27, 164, 210, 0);
    --ink-grey: #4a4a4a;
    --rule-grey: #b9b9b9;
    --card-white: #ffffff;
    --card-dark: #222222;
    --backdrop: #ececec;
    --text-white: #ffffff;
  }
  * { margin: 0; padding: 0; box-sizing: border-box; }
  html, body {
    width: 1200px; height: 987px; overflow: hidden;
    background: var(--backdrop);
  }
  .canvas { position: relative; width: 1200px; height: 987px; }

  .card {
    position: absolute; left: 293px; width: 615px; height: 351px;
    overflow: hidden;
  }
  .card--front { top: 130px; background: var(--card-white); }
  .card--back  { top: 505px; background: var(--card-dark); }

  /* front */
  .brand-name {
    position: absolute; right: 29px; top: 92px;
    font-family: "Roboto", Arial, sans-serif; font-weight: 700;
    font-size: 32px; letter-spacing: 0.5px; line-height: 1;
    color: var(--brand-blue);
    display: flex; align-items: center; gap: 10px;
  }
  .brand-dot {
    width: 22px; height: 22px; border-radius: 50%;
    background: var(--brand-blue);
  }
  .person-name {
    position: absolute; left: 34px; top: 222px;
    font-family: "Open Sans", Arial, sans-serif; font-weight: 600;
    font-size: 22px; color: var(--brand-blue); line-height: 1.2;
  }
  .name-rule {
    position: absolute; left: 34px; right: 29px; top: 252px;
    border-top: 1px solid var(--rule-grey);
  }
  .contact-list {
    position: absolute; left: 34px; top: 262px; list-style: none;
    font-family: "Open Sans", Arial, sans-serif; font-size: 16px;
    color: var(--ink-grey); line-height: 23px;
  }
  .contact-list li { display: flex; align-items: center; gap: 7px; }
  .contact-icon { width: 15px; height: 15px; flex: none; }
  .address {
    position: absolute; right: 29px; top: 265px; text-align: right;
    font-family: "Open Sans", Arial, sans-serif; font-size: 16px;
    color: var(--ink-grey); line-height: 22px; font-style: normal;
  }

  /* back */
  .back-artwork {
    position: absolute; left: 165px; top: 0; right: 0; bottom: 0;
    background: radial-gradient(ellipse 62% 58% at 58% 46%,
      var(--brand-blue-soft) 0%, var(--brand-blue-soft) 45%, var(--brand-blue-fade) 100%);
  }
  .back-brand {
    position: absolute; left: 30px; top: 268px; z-index: 1;
    font-family: "Roboto", Arial, sans-serif; font-weight: 700;
    font-size: 35px; color: var(--brand-blue); line-height: 1;
  }
  .back-web {
    position: absolute; left: 32px; top: 310px; z-index: 1;
    font-family: "Open Sans", Arial, sans-serif; font-size: 16px;
    letter-spacing: 3px; color: var(--text-white);
  }
</style>
</head>
<body>
<div class="canvas">

  <section class="card card--front">
    <div class="brand-name"><span class="brand-dot"></span>ROAM QUILL</div>

    <h1 class="person-name">Bertrand Olesky</h1>
    <div class="name-rule"></div>

    <ul class="contact-list">
      <li>
        <svg class="contact-icon" viewBox="0 0 16 16" aria-hidden="true">
          <path fill="#1ba4d2" d="M3.6 1.2l2.2 2.6c.3.4.3.9 0 1.3L4.6 6.4c.9 2 2.9 4 5 5l1.3-1.2c.4-.3.9-.3 1.3 0l2.6 2.2c.4.3.4.9.1 1.3l-1.3 1.4c-.5.5-1.3.7-2 .4C6.8 13.8 2.2 9.2.5 4.4.2 3.7.4 2.9.9 2.4L2.3 1.1c.4-.3 1-.3 1.3.1z"/>
        </svg>
        +1-(345)-402-7731
      </li>
      <li>
        <svg class="contact-icon" viewBox="0 0 16 16" aria-hidden="true">
          <rect x="1" y="3.5" width="14" height="9.5" fill="#1ba4d2"/>
          <path d="M1 3.8l7 5 7-5" fill="none" stroke="#fff" stroke-width="1.3"/>
        </svg>
        ceo@roamquill.net
      </li>
      <li>
        <svg class="contact-icon" viewBox="0 0 16 16" aria-hidden="true">
          <circle cx="8" cy="8" r="7" fill="#1ba4d2"/>
          <path d="M1 8h14M8 1c-2.5 2.5-2.5 11.5 0 14M8 1c2.5 2.5 2.5 11.5 0 14" fill="none" stroke="#fff" stroke-width="1"/>
        </svg>
        www.roamquill.net
      </li>
    </ul>

    <address class="address">
      Coral Reach Shore<br>
      Grand Cayman<br>
      Cayman Islands
    </address>
  </section>

  <section class="card card--back">
    <div class="back-artwork" role="img" aria-label="Large blue silhouette of the brand's travel animal mark, filling the right side of the card"></div>
    <div class="back-brand">ROAM QUILL</div>
    <div class="back-web">www.roamquill.net</div>
  </section>

</div>
</body>
</html>
```